Business card and stationary package

Travel management company looking for designs for single sided business cards, letterhead and envelope. Looking for contemporary designs using our existing logo. Design should clean, not trendy, no gradation of colors and no graphic other than the icon from the logo. Nothing complicated or difficult to read. Should be a crisp design using blue, gray and black colors only.
Letterhead should include a Word template and PDF template.
Business cards are one sided as the reverse will be dynamic images in our company portfolio of images.
We will use the same designer periodically for design projects using the same style guide for upcoming projects as well. Prefer working with designer that will assist with website, brochures and other marketing materials.

Logo Colors and Font:
Blue: 2189c6 Color Hex
Gray: 666666 Color Hex 60% Black
Black: 100% Black
Font: Century Gothic

Target Market(s)

business-to-business

Industry/Entity Type

Travel Industry

Contact Information for Business Card

Sample information for business cards will be:

Daniel Fenwick
Managing Partner

Harbourline Journey Solutions, Inc.
482 Alder Avenue, Suite 2307
Larkspur Falls, VT 05471

207-555-0148 Direct Dial
207-555-0172 Fax

daniel@harbourlinejs.net
www.harbourlinejs.net

Font styles to use
Sans Serif

Requirements
Must have
• Clean, crisp design, easy to ready, memorable.
Nice to have
• We tend to like dynamic designs that are simple, not trendy, contemporary and easy to read.
Should not have
• no gradation of colors and no graphic other than the icon from the logo, no background images
• **Note that the background should only be white. No black/gary backgrounds or graded colors**

```html
<!DOCTYPE html>
<html lang="en">
<head>
<meta charset="utf-8">
<title>Harbourline Journey Solutions – Business Card</title>
<link href="https://fonts.googleapis.com/css2?family=Questrial&family=Roboto:wght@400&display=swap" rel="stylesheet">
<style>
  :root {
    --brand-blue: #2189c6;
    --brand-gray: #666666;
    --brand-black: #000000;
    --card-white: #ffffff;
    --backdrop: #ecedef;
  }
  html, body {
    margin: 0;
    padding: 0;
    width: 1200px;
    height: 716px;
    overflow: hidden;
    background: var(--backdrop);
  }
  .stage {
    position: relative;
    width: 1200px;
    height: 716px;
  }
  .business-card {
    position: absolute;
    left: 180px;
    top: 118px;
    width: 840px;
    height: 480px;
    background: var(--card-white);
    box-shadow: 0 2px 10px rgba(0,0,0,0.12);
  }
  .holder {
    position: absolute;
    left: 52px;
    top: 50px;
  }
  .holder-name {
    margin: 0;
    font-family: "Questrial", sans-serif;
    font-size: 34px;
    font-weight: 400;
    color: var(--brand-blue);
    letter-spacing: 0.5px;
  }
  .holder-title {
    margin: 6px 0 0;
    font-family: "Roboto", sans-serif;
    font-size: 15px;
    color: var(--brand-gray);
  }
  .contact-list {
    position: absolute;
    left: 52px;
    top: 196px;
    margin: 0;
    padding: 0;
    list-style: none;
    font-family: "Roboto", sans-serif;
    font-size: 20px;
    line-height: 28px;
    color: var(--brand-gray);
  }
  .contact-item {
    display: flex;
    align-items: center;
  }
  .contact-icon {
    width: 16px;
    height: 16px;
    margin-right: 16px;
    fill: var(--brand-blue);
    flex: none;
  }
  .address {
    position: absolute;
    left: 52px;
    top: 308px;
    margin: 0;
    font-family: "Roboto", sans-serif;
    font-style: normal;
    font-size: 20px;
    line-height: 28px;
    color: var(--brand-gray);
  }
  .brand-mark {
    position: absolute;
    left: 520px;
    top: 170px;
    width: 270px;
    display: flex;
    flex-direction: column;
    align-items: center;
  }
  .brand-dot {
    width: 110px;
    height: 110px;
    border-radius: 50%;
    background: var(--brand-blue);
  }
  .brand-name {
    margin-top: 22px;
    font-family: "Questrial", sans-serif;
    font-size: 24px;
    line-height: 30px;
    color: var(--brand-blue);
    text-align: center;
  }
</style>
</head>
<body>
<main class="stage">
  <article class="business-card">
    <header class="holder">
      <h1 class="holder-name">Daniel Fenwick</h1>
      <p class="holder-title">Managing Partner</p>
    </header>

    <ul class="contact-list">
      <li class="contact-item">
        <svg class="contact-icon" viewBox="0 0 16 16" aria-hidden="true"><path d="M3.5 1l2.5 3-1.5 1.6c.9 2 2.5 3.6 4.4 4.4L10.5 8.5l3 2.5-1.3 3C7 13.6 2.4 9 2 3.8z"/></svg>
        <span>207-555-0148</span>
      </li>
      <li class="contact-item">
        <svg class="contact-icon" viewBox="0 0 16 16" aria-hidden="true"><rect x="4" y="1" width="8" height="4"/><rect x="1" y="6" width="14" height="6" rx="1"/><rect x="4" y="10" width="8" height="5"/></svg>
        <span>207-555-0172</span>
      </li>
      <li class="contact-item">
        <svg class="contact-icon" viewBox="0 0 16 16" aria-hidden="true"><path d="M1 3h14v10H1z M2 4l6 5 6-5" stroke="#fff" stroke-width="1"/></svg>
        <span>daniel@harbourlinejs.net</span>
      </li>
      <li class="contact-item">
        <svg class="contact-icon" viewBox="0 0 16 16" aria-hidden="true"><circle cx="8" cy="8" r="7"/><path d="M1 8h14M8 1v14M3 4h10M3 12h10" stroke="#fff" stroke-width="1" fill="none"/></svg>
        <span>www.harbourlinejs.net</span>
      </li>
    </ul>

    <address class="address">
      482 Alder Avenue, Suite 2307<br>
      Larkspur Falls, VT 05471
    </address>

    <div class="brand-mark">
      <div class="brand-dot"></div>
      <div class="brand-name">Harbourline Journey Solutions, Inc.</div>
    </div>
  </article>
</main>
</body>
</html>
```